Wine Label for White and Red Wine from California

We need a wine label for 2 whites and 2 red wines. (Merlot, Cabernet Sauvignon, Chardonnay, Pinot Grigio) Can be the same label or can have something to differentiate among them such as a color change. This is a label for an already existing wine on the US market but needs to be completely re-done. We want something way sharper, eye catching. Don't use the original label please as your starting point-- I don't think we want to see it anymore. But the structure of it is ok and the fonts are ok. (The tree is what is so awful about)

Target Market(s)

US market, always good to think of millennials, but still appeal to all ages. Men and women.

Colors

Designer to choose colors to be used in the design.

Requirements
Must have
• Should be eye catching, grabs attention, looks expensive, sells for a value price. Should feature the brand name and varietal and vintage:
• Dorvane Vineyards / Cabernet Sauvignon / 2014
• Bottle type is the 'Bordeaux Style' bottle. The white wine is a green bottle, the red wine uses a dark brown bottle. Be sure the labels look good on these bottles.
• What this bottle looks like is shown below.
• The label we are replacing is shown in the briefs.
Nice to have
• We feel successful labels have a lot of white background, stay away from dark labels-- they scratch too much when handled.
• Attached is a label we like, please look at the Cadenza label image below. But at the same time, we are flexible to your creativity. But nothing too crazy please.
Should not have
• Should not have a dark background.
• We are not big fans of grapes on the label unless extremely stylised. Nor do we like wine glasses, wine bottles.

```html
<!DOCTYPE html>
<html lang="en">
<head>
<meta charset="utf-8">
<title>Dorvane Vineyards — Label Range</title>
<link href="https://fonts.googleapis.com/css2?family=Cinzel:wght@400;600&family=Cormorant+Garamond:wght@500&display=swap" rel="stylesheet">
<style>
  :root {
    --backdrop: #a7a7a7;
    --paper: #f7f7f5;
    --brand-gold: #a6977a;
    --ink-muted: #5e5e5e;
    --ink-vintage: #3a3a3a;
    --cabernet: #8c2a34;
    --cabernet-vein: #a9444d;
    --merlot: #1b1b1b;
    --merlot-vein: #3a3a3a;
    --pinot: #41695f;
    --pinot-vein: #5c8479;
    --chardonnay-light: #cdb994;
    --chardonnay-dark: #2b231b;
    --chardonnay-ink: #4a3e30;
    --frame-line: rgba(255,255,255,0.85);
  }
  * { box-sizing: border-box; margin: 0; padding: 0; }
  html, body { width: 801px; height: 1200px; overflow: hidden; }
  body {
    background: var(--backdrop);
    display: flex;
    align-items: center;
    justify-content: center;
  }
  .label-range {
    display: flex;
    gap: 20px;
  }
  .label {
    position: relative;
    width: 170px;
    height: 272px;
    background: var(--paper);
    box-shadow: 0 2px 6px rgba(0,0,0,0.18);
  }
  .varietal-panel {
    position: absolute;
    top: 0;
    left: 37px;
    width: 96px;
    height: 158px;
    padding: 6px 14px;
  }
  .leaf-pattern {
    width: 100%;
    height: 100%;
    border: 1px solid var(--frame-line);
  }
  .label--cabernet .varietal-panel { background: var(--cabernet); }
  .label--cabernet .leaf-pattern { background: var(--cabernet-vein); }
  .label--merlot .varietal-panel { background: var(--merlot); }
  .label--merlot .leaf-pattern { background: var(--merlot-vein); }
  .label--pinot .varietal-panel { background: var(--pinot); }
  .label--pinot .leaf-pattern { background: var(--pinot-vein); }
  .label--chardonnay .varietal-panel {
    background: linear-gradient(90deg, var(--chardonnay-light), #8a7858 55%, var(--chardonnay-dark));
  }
  .label--chardonnay .leaf-pattern {
    background: linear-gradient(90deg, #d9c9a8, #9a8969 55%, #4a3e30);
  }
  .brand-name {
    position: absolute;
    top: 172px;
    width: 100%;
    text-align: center;
    font-family: "Cinzel", serif;
    font-weight: 600;
    font-size: 21px;
    line-height: 24px;
    letter-spacing: 3px;
    color: var(--brand-gold);
  }
  .brand-sub {
    position: absolute;
    top: 199px;
    width: 100%;
    text-align: center;
    font-family: "Cormorant Garamond", serif;
    font-size: 7.5px;
    line-height: 9px;
    letter-spacing: 3.5px;
    color: var(--ink-muted);
  }
  .vintage {
    position: absolute;
    top: 212px;
    width: 100%;
    text-align: center;
    font-family: "Cinzel", serif;
    font-weight: 400;
    font-size: 11px;
    line-height: 14px;
    letter-spacing: 2px;
    color: var(--ink-vintage);
  }
  .varietal-name {
    position: absolute;
    top: 237px;
    width: 100%;
    text-align: center;
    font-family: "Cinzel", serif;
    font-weight: 600;
    font-size: 10.5px;
    line-height: 14px;
    letter-spacing: 0.2px;
    white-space: nowrap;
  }
  .label--cabernet .varietal-name { color: var(--cabernet); }
  .label--merlot .varietal-name { color: var(--merlot); font-size: 12px; }
  .label--pinot .varietal-name { color: var(--pinot); }
  .label--chardonnay .varietal-name { color: var(--chardonnay-ink); }
</style>
</head>
<body>
  <main class="label-range">
    <article class="label label--cabernet">
      <div class="varietal-panel"><div class="leaf-pattern" role="img" aria-label="Leaf vein pattern in deep red"></div></div>
      <h1 class="brand-name">DORVANE</h1>
      <p class="brand-sub">VINEYARDS</p>
      <p class="vintage">2014</p>
      <p class="varietal-name">CABERNET SAUVIGNON</p>
    </article>
    <article class="label label--merlot">
      <div class="varietal-panel"><div class="leaf-pattern" role="img" aria-label="Leaf vein pattern in black"></div></div>
      <h1 class="brand-name">DORVANE</h1>
      <p class="brand-sub">VINEYARDS</p>
      <p class="vintage">2014</p>
      <p class="varietal-name">MERLOT</p>
    </article>
    <article class="label label--pinot">
      <div class="varietal-panel"><div class="leaf-pattern" role="img" aria-label="Leaf vein pattern in sage green"></div></div>
      <h1 class="brand-name">DORVANE</h1>
      <p class="brand-sub">VINEYARDS</p>
      <p class="vintage">2014</p>
      <p class="varietal-name">PINOT GRIGIO</p>
    </article>
    <article class="label label--chardonnay">
      <div class="varietal-panel"><div class="leaf-pattern" role="img" aria-label="Leaf vein pattern in gold fading to brown"></div></div>
      <h1 class="brand-name">DORVANE</h1>
      <p class="brand-sub">VINEYARDS</p>
      <p class="vintage">2014</p>
      <p class="varietal-name">CHARDONNAY</p>
    </article>
  </main>
</body>
</html>
```